Tech business card design

We need an amazing business card design for our new business 'Brakka' a marketing tech startup based in Sydney, Australia. We provide an online marketplace for businesses to search and buy advertising media, connect with service providers and learn more about marketing. We wish to communicate 'cool tech', reliability and professionalism and design based around our logo.

Target Market(s)

Business Owners

Contact Information for Business Card

Name
Position
Email Address
Website
Phone Number

Font styles to use
Other font styles liked:
• Avenir & Avenir Next

Colors

Designer to choose colors to be used in the design.

```html
<!DOCTYPE html>
<html lang="en">
<head>
<meta charset="utf-8">
<title>Brakka business card</title>
<link rel="stylesheet" href="https://fonts.googleapis.com/css2?family=Nunito+Sans:wght@400;600;800&display=swap">
<style>
  :root {
    --navy: #11113a;
    --navy-band: #25264a;
    --white: #ffffff;
    --backdrop: #e6e6e6;
    --card-shadow: 0 3px 10px rgba(0, 0, 0, 0.28);
  }
  * { box-sizing: border-box; margin: 0; padding: 0; }
  html, body {
    width: 1125px;
    height: 1200px;
    overflow: hidden;
    background: var(--backdrop);
    font-family: "Nunito Sans", "Avenir Next", Avenir, sans-serif;
  }
  .card {
    position: absolute;
    left: 171px;
    width: 800px;
    height: 456px;
    transform-origin: 0 0;
    transform: scale(1.0325);
    box-shadow: var(--card-shadow);
    overflow: hidden;
  }
  .card--front { top: 106px; background: var(--white); }
  .card--back { top: 639px; background: var(--navy); }

  .front-shapes { position: absolute; inset: 0; width: 100%; height: 100%; }

  .wordmark {
    position: absolute;
    font-weight: 800;
    letter-spacing: -1px;
    line-height: 1;
  }
  .card--front .wordmark {
    right: 82px;
    top: 56px;
    font-size: 108px;
    color: var(--navy);
  }
  .card--back .wordmark {
    right: 54px;
    top: 330px;
    font-size: 66px;
    color: var(--white);
  }

  .identity {
    position: absolute;
    left: 49px;
    top: 282px;
    color: var(--white);
  }
  .identity__name {
    font-size: 27px;
    font-weight: 600;
    letter-spacing: 0.3px;
    line-height: 1.1;
  }
  .identity__role {
    font-size: 20px;
    font-weight: 400;
    letter-spacing: 0.4px;
    line-height: 1.2;
  }
  .contact {
    list-style: none;
    margin-top: 14px;
  }
  .contact__item {
    display: flex;
    align-items: center;
    gap: 12px;
    font-size: 17.5px;
    line-height: 25.5px;
  }
  .contact__icon { width: 18px; height: 18px; flex: none; }

  .pattern-fill {
    position: absolute;
    inset: 0;
    background: var(--navy);
  }
</style>
</head>
<body>

<section class="card card--front">
  <svg class="front-shapes" viewBox="0 0 800 456" preserveAspectRatio="none" aria-hidden="true">
    <polygon points="0,251 322,251 464,456 0,456" fill="var(--navy)"/>
    <polygon points="462,432 800,432 800,456 478,456" fill="var(--navy-band)"/>
  </svg>

  <div class="wordmark">brakka</div>

  <div class="identity">
    <h1 class="identity__name">DANIEL MOSS</h1>
    <p class="identity__role">FOUNDER, DIRECTOR</p>
    <ul class="contact">
      <li class="contact__item">
        <svg class="contact__icon" viewBox="0 0 18 18" aria-hidden="true">
          <rect x="4.5" y="1" width="9" height="16" rx="1.5" fill="none" stroke="#fff" stroke-width="1.6"/>
          <rect x="6" y="3" width="6" height="10" fill="#fff"/>
        </svg>
        +61 (0)400 555 019
      </li>
      <li class="contact__item">
        <svg class="contact__icon" viewBox="0 0 18 18" aria-hidden="true">
          <rect x="2" y="5" width="14" height="9" fill="#fff"/>
          <polyline points="2,5 9,10.5 16,5" fill="none" stroke="var(--navy)" stroke-width="1.3"/>
        </svg>
        daniel@brakkamedia.com.au
      </li>
      <li class="contact__item">
        <svg class="contact__icon" viewBox="0 0 18 18" aria-hidden="true">
          <circle cx="9" cy="9" r="7.5" fill="#fff"/>
          <path d="M5 6 Q7 4 9 6 Q8 9 6 9 Z M10 10 Q13 9 13.5 12 Q11 14.5 10 12 Z" fill="var(--navy)"/>
        </svg>
        www.brakkamedia.com.au
      </li>
    </ul>
  </div>
</section>

<section class="card card--back">
  <div class="pattern-fill" role="img" aria-label="Faint repeated brand name pattern across the navy back"></div>
  <div class="wordmark">brakka</div>
</section>

</body>
</html>
```